Leading In-Home Tutoring Company Needs Web Banners

We need a suite of web banners for our re-marketing campaign. We are based in Melbourne and heading into the busiest time of the year with back to school and we would like to help guide parents to working with us via quality designed banners with the right CTAs. Banner specs as follows (W x H in pixels)
Medium Rectangle: 300 x 250
Vertical rectangle: 240 x 400
Banner: 468 x 60
Leaderboard: 728 x 90
Square: 250 x 250
Mobile leaderboard: 320 x 50
Updates

Hi designers I'm new to this and didn't realise that I had to upload all files at the beginning. I have images that can be used for this project. Just need to work out how to upload them. Added Sunday, January 22, 2017

Hi awesome designers... I've updated the brief now with new files :)

Target Market(s)

Mothers who value kids education. Our customer can be found having morning coffee with friends in her lycra as she prepares to go to the gym. Middle class, inner city and suburban Mums. Most likely on Friendnook.

Industry/Entity Type

It Company

Font styles to use
Sans Serif

Colors
0692cd
fbed22
f47f39
ec1f27

Requirements
Must have
• Wording should include.
• What we do: 1:1, In-Home Tutoring
• Value proposition: The Best Tutor For Your Child
• Call to Action - Free Assessment > Find Out More
• Adjusted layout to suit the sizes. Use of image where possible to provide immediate graphic display of what we do
Nice to have
• Keep it simple, create an emotive connection. Kids matter to parents and they will pay for services if we can create banners that show we care and can help wtih their education.
Should not have
• Anything negative or use fear marketing

```html
<!DOCTYPE html>
<html lang="en">
<head>
<meta charset="utf-8">
<title>TutorNest – Web Banner Suite</title>
<link rel="stylesheet" href="https://fonts.googleapis.com/css2?family=Open+Sans:wght@400;700;800&family=Roboto+Condensed:wght@400&display=swap">
<style>
  :root{
    --page-top:#ececec;
    --page-bottom:#dcdcdc;
    --label:#3f3f3f;
    --band-dark:#0b3f5e;
    --band-mid:#0a5d88;
    --brand-blue:#0692cd;
    --badge-blue:#1a8fd0;
    --white:#ffffff;
    --accent-orange:#f47f39;
    --photo-warm:#b58a68;
    --photo-cool:#4f7fa8;
    --photo-light:#d9d3c8;
  }
  *{box-sizing:border-box;margin:0;padding:0}
  html,body{width:855px;height:1200px;overflow:hidden}
  body{
    position:relative;
    background:linear-gradient(160deg,var(--page-top),var(--page-bottom));
    font-family:"Open Sans",Arial,sans-serif;
    color:var(--white);
  }
  .ad{position:absolute;overflow:hidden;background:linear-gradient(90deg,var(--band-dark),var(--band-mid) 60%,var(--brand-blue))}
  .photo{position:absolute;background:linear-gradient(135deg,var(--photo-cool) 0%,var(--photo-light) 40%,var(--photo-warm) 75%,var(--photo-cool) 100%)}
  .band{position:absolute;left:0;right:0;bottom:0;background:linear-gradient(90deg,var(--band-dark),var(--band-mid) 55%,var(--brand-blue))}
  .badge{
    position:absolute;border-radius:50%;
    background:radial-gradient(circle at 40% 35%,#3aaee6,var(--badge-blue) 60%,#0c6fa8);
    display:flex;align-items:center;justify-content:center;
    font-weight:800;color:var(--white);
  }
  .service{position:absolute;font-weight:800;color:var(--white);text-shadow:0 1px 3px rgba(0,0,0,.55);line-height:1}
  .tagline{position:absolute;line-height:1.25;color:var(--white)}
  .tagline strong{font-weight:800}
  .brand{position:absolute;display:flex;align-items:center;gap:5px;font-weight:700;color:var(--white);line-height:1}
  .brand-dot{border-radius:50%;background:var(--accent-orange);flex:none}
  .size-label{
    position:absolute;transform:translateX(-50%);white-space:nowrap;
    font-family:"Roboto Condensed",Arial,sans-serif;font-size:21px;color:var(--label);
  }

  /* Leaderboard 728x90 */
  .leaderboard{left:73px;top:66px;width:699px;height:87px}
  .leaderboard .photo{left:0;top:0;width:248px;height:100%}
  .leaderboard .badge{left:2px;top:50px;width:36px;height:36px;font-size:15px}
  .leaderboard .service{left:44px;top:65px;font-size:15px}
  .leaderboard .tagline{left:261px;top:22px;font-size:19px}
  .leaderboard .brand{right:44px;top:52px;font-size:26px}
  .leaderboard .brand-dot{width:12px;height:12px}

  /* Banner 468x60 */
  .banner{left:74px;top:231px;width:450px;height:56px}
  .banner .photo{left:0;top:0;width:157px;height:100%}
  .banner .badge{left:-6px;top:-6px;width:34px;height:34px;font-size:13px;padding:4px 0 0 6px}
  .banner .service{left:6px;top:38px;font-size:13px}
  .banner .tagline{left:168px;top:14px;font-size:12.5px}
  .banner .brand{right:22px;top:34px;font-size:15px}
  .banner .brand-dot{width:8px;height:8px}

  /* Mobile leaderboard 320x50 */
  .mobile{left:73px;top:369px;width:306px;height:48px}
  .mobile .badge{left:0;top:2px;width:40px;height:40px;font-size:17px}
  .mobile .service{left:50px;top:12px;font-size:15px;text-shadow:none}
  .mobile .brand{right:10px;top:29px;font-size:14px}
  .mobile .brand-dot{width:8px;height:8px}

  /* Medium rectangle 300x250 */
  .medium{left:73px;top:533px;width:288px;height:240px}
  .medium .photo{inset:0 0 55px 0}
  .medium .band{height:55px}
  .medium .badge{left:-8px;top:-12px;width:74px;height:74px;font-size:27px;padding:10px 0 0 8px}
  .medium .service{left:69px;top:21px;font-size:20px}
  .medium .tagline{left:11px;top:14px;font-size:12.5px}
  .medium .brand{right:10px;top:30px;font-size:15px}
  .medium .brand-dot{width:9px;height:9px}

  /* Vertical rectangle 240x400 */
  .vertical{left:540px;top:534px;width:230px;height:384px}
  .vertical .photo{inset:0 0 126px 0}
  .vertical .band{height:126px}
  .vertical .badge{left:-8px;top:-12px;width:72px;height:72px;font-size:26px;padding:10px 0 0 8px}
  .vertical .service{left:66px;top:11px;font-size:21px;line-height:1.05}
  .vertical .tagline{left:13px;top:11px;font-size:15.5px;line-height:1.4}
  .vertical .brand{right:14px;top:92px;font-size:21px}
  .vertical .brand-dot{width:12px;height:12px}

  /* Square 250x250 */
  .square{left:74px;top:867px;width:240px;height:240px}
  .square .photo{inset:0 0 55px 0}
  .square .band{height:55px}
  .square .badge{left:-8px;top:-10px;width:66px;height:66px;font-size:24px;padding:8px 0 0 8px}
  .square .service{left:62px;top:21px;font-size:17px}
  .square .tagline{left:9px;top:7px;font-size:11px}
  .square .brand{right:10px;top:33px;font-size:14px}
  .square .brand-dot{width:8px;height:8px}
</style>
</head>
<body>

<section class="ad leaderboard" aria-label="Leaderboard banner">
  <div class="photo" role="img" aria-label="Tutor and schoolboy working together at a desk in front of a bookshelf"></div>
  <div class="badge">1:1</div>
  <div class="service">In-home tutoring</div>
  <p class="tagline">The best tutor for your child<br>with <strong>free</strong> assessment.</p>
  <div class="brand"><span class="brand-dot"></span>TutorNest</div>
</section>
<div class="size-label" style="left:424px;top:168px">Leaderboard: 728 x 90</div>

<section class="ad banner" aria-label="Banner">
  <div class="photo" role="img" aria-label="Tutor and schoolboy working together at a desk"></div>
  <div class="badge">1:1</div>
  <div class="service">In-home tutoring</div>
  <p class="tagline">The best tutor for your child<br>with <strong>free</strong> assessment.</p>
  <div class="brand"><span class="brand-dot"></span>TutorNest</div>
</section>
<div class="size-label" style="left:288px;top:300px">Banner: 468 x 60</div>

<section class="ad mobile" aria-label="Mobile leaderboard">
  <div class="badge">1:1</div>
  <div class="service">In-home tutoring</div>
  <div class="brand"><span class="brand-dot"></span>TutorNest</div>
</section>
<div class="size-label" style="left:226px;top:428px">Mobile leaderboard: 320 x 50</div>

<section class="ad medium" aria-label="Medium rectangle">
  <div class="photo" role="img" aria-label="Tutor and schoolboy smiling over a workbook in front of a bookshelf"></div>
  <div class="badge">1:1</div>
  <div class="service">In-home tutoring</div>
  <div class="band">
    <p class="tagline">The best tutor for your child<br>with <strong>free</strong> assessment.</p>
    <div class="brand"><span class="brand-dot"></span>TutorNest</div>
  </div>
</section>
<div class="size-label" style="left:215px;top:787px">Medium Rectangle: 300 x 250</div>

<section class="ad vertical" aria-label="Vertical rectangle">
  <div class="photo" role="img" aria-label="Female tutor and schoolboy laughing together while writing at a desk"></div>
  <div class="badge">1:1</div>
  <div class="service">In-home<br>tutoring</div>
  <div class="band">
    <p class="tagline">The best tutor for your child<br>with <strong>free</strong> assessment.</p>
    <div class="brand"><span class="brand-dot"></span>TutorNest</div>
  </div>
</section>
<div class="size-label" style="left:654px;top:931px">Vertical rectangle: 240 x 400</div>

<section class="ad square" aria-label="Square">
  <div class="photo" role="img" aria-label="Tutor and schoolboy working together over a workbook"></div>
  <div class="badge">1:1</div>
  <div class="service">In-home tutoring</div>
  <div class="band">
    <p class="tagline">The best tutor for your child<br>with <strong>free</strong> assessment.</p>
    <div class="brand"><span class="brand-dot"></span>TutorNest</div>
  </div>
</section>
<div class="size-label" style="left:179px;top:1119px">Square: 250 x 250</div>

</body>
</html>
```